Marcus Pellow Carpentry & Joinery

Hello, I would like a flyer designed for my new business doing small projects in my local area for home-owners. I am a professional tradesman.
The type of work I am offering is:
- decks/decking
- external stairs & railings
- install windows & doors
- roofs & gutters
- small additions
- built-in wardrobes
- finish work
- demolition

It would be great if the flyer could mention these, or use phrasing that fits this kind of construction work.
My idea for a slogan was "new work and repairs to any age home".

Please also mention FREE QUOTES and have my email and phone number included on the flyer, along with my carpentry licence number, which I can provided.

I'd like a one page, single-sided flyer that could be printed as DL.
Colour and style is up to you! I'll be placing this flyer on counters & in the windows of local businesses, so something simple and eye-catching is preferred.

Thank you!

```html
<!DOCTYPE html>
<html lang="en">
<head>
<meta charset="utf-8">
<title>Marcus Pellow Carpentry &amp; Joinery – Flyer</title>
<link href="https://fonts.googleapis.com/css2?family=Marcellus&family=Ruluko&display=swap" rel="stylesheet">
<style>
  :root {
    --page-bg: #e4e2df;
    --panel-bg: #f3f3f3;
    --gap-white: #ffffff;
    --brand-blue: #2ea6dc;
    --ink-brown: #4b3a30;
    --list-brown: #5b463a;
    --rule-brown: #8b6d58;
    --white: #ffffff;
  }
  * { box-sizing: border-box; margin: 0; padding: 0; }
  html, body {
    width: 1200px; height: 645px; overflow: hidden;
    background: var(--page-bg);
  }
  .canvas { position: relative; width: 1200px; height: 645px; }
  .flyer {
    position: absolute; left: 40px; top: 50px;
    width: 1118px; height: 532px;
    background: var(--panel-bg);
    overflow: hidden;
    font-family: "Ruluko", sans-serif;
  }
  .photo-grid {
    position: absolute; left: 0; top: 0; width: 573px; height: 532px;
    background: var(--gap-white);
  }
  .photo { position: absolute; }
  .photo--deck { left: 0; top: 0; width: 285px; height: 260px;
    background: linear-gradient(180deg, #5f7f45 0%, #8a6a44 30%, #a9744a 60%, #9c6a40 100%); }
  .photo--stairs { left: 290px; top: 0; width: 283px; height: 260px;
    background: linear-gradient(180deg, #ece8e2 0%, #d8cfc4 55%, #8a6448 85%, #e9e5df 100%); }
  .photo--wardrobe { left: 0; top: 265px; width: 285px; height: 267px;
    background: linear-gradient(180deg, #e2c08c 0%, #d7b17a 55%, #c9a06a 100%); }
  .photo--window { left: 290px; top: 265px; width: 283px; height: 267px;
    background: linear-gradient(180deg, #c9a57a 0%, #a9c3d6 18%, #7b9a5a 48%, #b58a5c 78%, #ece3d4 100%); }
  .guarantee-seal { position: absolute; left: 248px; top: 225px; width: 80px; height: 80px; }

  .brand-name {
    position: absolute; right: 36px; top: 33px;
    font-family: "Marcellus", serif; font-size: 28px; line-height: 34px;
    color: var(--brand-blue); text-align: right; font-weight: 400;
  }
  .slogan {
    position: absolute; left: 600px; top: 137px; width: 472px;
    border-top: 2px solid var(--rule-brown); border-bottom: 2px solid var(--rule-brown);
    padding: 9px 0 8px; text-align: center;
    font-size: 29px; line-height: 32px; color: var(--ink-brown); white-space: nowrap;
  }
  .services-heading {
    position: absolute; left: 613px; top: 213px;
    display: flex; align-items: center; gap: 6px;
    font-size: 25px; font-weight: 400; color: var(--brand-blue);
  }
  .service-list {
    position: absolute; top: 256px; list-style: none;
    font-size: 21.5px; line-height: 36.5px; color: var(--list-brown);
  }
  .service-list li::before { content: "» "; }
  .service-list--left { left: 640px; }
  .service-list--right { left: 908px; }
  .licence {
    position: absolute; right: 40px; top: 428px;
    font-size: 17px; color: var(--ink-brown);
  }
  .contact-band {
    position: absolute; left: 617px; top: 455px; width: 501px; height: 77px;
    background: var(--brand-blue); border-top-left-radius: 32px;
    color: var(--white); text-align: center;
  }
  .contact-call {
    margin-top: 10px; font-size: 19px;
    display: flex; justify-content: center; align-items: center; gap: 8px;
  }
  .contact-email { font-size: 15px; margin-top: 4px; }
</style>
</head>
<body>
<div class="canvas">
  <div class="flyer">
    <div class="photo-grid">
      <div class="photo photo--deck" role="img" aria-label="Photo: timber deck with built-in bench seating and garden hedge"></div>
      <div class="photo photo--stairs" role="img" aria-label="Photo: timber staircase with iron balusters and white risers"></div>
      <div class="photo photo--wardrobe" role="img" aria-label="Photo: built-in timber wardrobe with hanging clothes, shelves and drawers"></div>
      <div class="photo photo--window" role="img" aria-label="Photo: timber-framed windows overlooking green hills"></div>
      <svg class="guarantee-seal" viewBox="0 0 80 80" aria-hidden="true">
        <circle cx="40" cy="40" r="37" fill="#ffffff" stroke="#2ea6dc" stroke-width="4"/>
      </svg>
    </div>

    <h1 class="brand-name">Marcus Pellow<br>Carpentry &amp; Joinery</h1>

    <p class="slogan">New Work and Repairs to any age home!</p>

    <h2 class="services-heading">
      <svg width="20" height="20" viewBox="0 0 20 20" aria-hidden="true">
        <circle cx="10" cy="10" r="10" fill="var(--brand-blue)"/>
        <path d="M8 5.5 L12.5 10 L8 14.5" fill="none" stroke="#fff" stroke-width="2.6"/>
      </svg>
      Services:
    </h2>
    <ul class="service-list service-list--left">
      <li>decks/decking</li>
      <li>external stairs &amp; railings</li>
      <li>install windows &amp; doors</li>
      <li>roofs &amp; gutters</li>
    </ul>
    <ul class="service-list service-list--right">
      <li>small additions</li>
      <li>built-in wardrobes</li>
      <li>finish work</li>
      <li>demolition</li>
    </ul>

    <p class="licence">Licence number: 4719305</p>

    <div class="contact-band">
      <p class="contact-call">Call us now for a FREE QUOTES:
        <svg width="22" height="22" viewBox="0 0 22 22" aria-hidden="true">
          <circle cx="11" cy="11" r="9.5" fill="none" stroke="#fff" stroke-width="2"/>
          <path d="M7.6 6 L9.4 6 L10.2 8.6 L9 9.6 Q10 12 12.4 13 L13.4 11.8 L16 12.6 L16 14.4 Q15 16 13 15.6 Q7.4 14 6.4 8.6 Q6.2 6.8 7.6 6 Z" fill="#fff"/>
        </svg>
        0400 555 218</p>
      <p class="contact-email">email: marcus.pellow@pellowjoinery.com mobile</p>
    </div>
  </div>
</div>
</body>
</html>
```